Come Play With Us!!! We are the Elite

We need a hiring flyer to hand out to potential recruits.
Please promote our social pages.
Something attractive, and informative with calls to action to contact us.
Please promote for people to follow us on social media.
We would like to list the following advantages to work here:
• Industry Leading Compensation
• Structured Career Advancement
• Safe Work Environment
• Work Promise Policy (Full Time Staff)
• Health & Dental Benefits
• Paid Training Programs
• Paid Clothing Allowance
• Paid Boot Allowance
• Positive Culture
• Progressive Culture
• Equal Opportunity Employer
• Veteran Friendly Employer
• New Equipment
• Paid Leadership Training
• Transparent Communication
• Community Focused
• Prestigious Clientele
• Local Work
• Focused on using industry leading tech
• Tool Purchase Program
• Family Atmosphere
• Team Events (Sports games, Lunches, Get togethers, Etc)
• Work Life balance
• Daily On Call Snow Pay
- Sick Pay
- Positive reputation
• Bonus’s available:
o Winter Shift Premium
o Referral Bonus
o Project Incentives
Current Positions open:
- Winter Crew Members
- Salt Truck Driver/Operator (AZ/DZ/AR)
- Winter Equipment Operators
- Construction Foreperson
Landscape and Construction

```html
<!DOCTYPE html>
<html lang="en">
<head>
<meta charset="utf-8">
<title>Ridgeline Contracting Group – We Are Hiring</title>
<link rel="stylesheet" href="https://fonts.googleapis.com/css2?family=Oswald:wght@600;700&family=Montserrat:wght@400;500;600;700&display=swap">
<style>
  :root{
    --green-dark:#1f6a2f;
    --green-lime:#8cc63f;
    --charcoal:#2b2b2b;
    --ink:#1d1d1d;
    --paper:#ffffff;
    --rule:#cfd6cf;
  }
  *{box-sizing:border-box;margin:0;padding:0}
  html,body{width:680px;height:1200px;overflow:hidden;background:var(--paper)}
  body{font-family:"Montserrat",sans-serif;color:var(--ink)}
  .flyer{position:relative;width:680px;height:1200px;background:var(--paper)}

  /* brand */
  .brand{position:absolute;left:44px;top:34px;display:flex;align-items:center;gap:12px}
  .brand-ring{width:66px;height:66px;border:5px solid var(--ink);border-radius:50%}
  .brand-name{font-weight:500;font-size:17px;line-height:1.08;letter-spacing:1.5px;color:var(--ink);text-transform:uppercase}

  /* header */
  .hero-band{position:absolute;left:0;top:138px;width:335px;height:272px;background:var(--green-dark)}
  .hero-title{position:absolute;left:44px;top:160px;width:285px;font-family:"Oswald",sans-serif;font-weight:700;font-size:92px;line-height:1.02;color:var(--paper);letter-spacing:-1px;text-transform:uppercase;white-space:nowrap}
  .hero-strip{position:absolute;right:0;top:138px;width:44px;height:272px;background:var(--green-dark)}
  .photo{position:absolute;display:block}
  .photo-crew{left:340px;top:30px;width:290px;height:380px;background:linear-gradient(180deg,#c9d8e6 0%,#8fae7a 38%,#d8e84a 55%,#5f8a3a 78%,#4a7030 100%)}

  /* advantages */
  .adv-heading{position:absolute;left:44px;top:438px;font-size:21px;font-weight:400;letter-spacing:-.2px;text-transform:uppercase;color:var(--ink)}
  .adv-heading strong{font-weight:700;color:var(--green-dark)}
  .adv-list{position:absolute;top:480px;list-style:none;font-size:10px;font-weight:500;line-height:1.25;letter-spacing:-.15px}
  .adv-list li{position:relative;padding-left:18px;margin-bottom:9px}
  .adv-list li.tick::before{content:"";position:absolute;left:0;top:0;width:12px;height:12px;border:1.4px solid var(--green-dark);border-radius:50%}
  .adv-list li.tick::after{content:"";position:absolute;left:4.3px;top:2.6px;width:3px;height:5.5px;border:solid var(--green-dark);border-width:0 1.6px 1.6px 0;transform:rotate(45deg)}
  .adv-list li.dot::before{content:"";position:absolute;left:4px;top:4px;width:5px;height:5px;border-radius:50%;background:var(--green-dark)}
  .adv-list li.plain{padding-left:30px}
  .col-one{left:44px;width:226px;white-space:nowrap}
  .col-two{left:282px;width:178px}
  .col-three{left:476px;width:166px;top:484px}
  .col-rule{position:absolute;top:478px;width:1px;height:225px;background:var(--rule)}
  .rule-a{left:274px}
  .rule-b{left:468px}

  /* photo strip */
  .side-block{position:absolute;top:795px;width:44px;height:72px;background:var(--charcoal)}
  .side-left{left:0}
  .side-right{right:0}
  .photo-paving{left:52px;top:742px;width:184px;height:176px;background:linear-gradient(160deg,#7c7f86 0%,#b7b2a6 45%,#5a5a5a 100%)}
  .photo-yard{left:243px;top:742px;width:183px;height:176px;background:linear-gradient(180deg,#3f6c33 0%,#d9ea3c 45%,#5e9a3b 100%)}
  .photo-van{left:433px;top:742px;width:197px;height:176px;background:linear-gradient(180deg,#9fb0bf 0%,#f2f4f4 40%,#dfe3e3 75%,#555 100%)}

  /* bonus */
  .bonus{position:absolute;left:44px;top:950px;width:166px;border-radius:6px;overflow:hidden;background:var(--charcoal);box-shadow:0 3px 6px rgba(0,0,0,.35)}
  .bonus-title{background:var(--green-lime);font-family:"Oswald",sans-serif;font-weight:600;font-size:19px;line-height:1;color:var(--ink);text-align:center;padding:10px 0;text-transform:uppercase;letter-spacing:-.4px;white-space:nowrap}
  .bonus-list{list-style:none;padding:6px 12px 10px}
  .bonus-list li{color:var(--paper);font-size:10.5px;font-weight:600;text-align:center;padding:10px 0;border-bottom:1px solid #444}
  .bonus-list li:last-child{border-bottom:none}

  /* positions */
  .positions{position:absolute;left:224px;top:950px;width:284px}
  .positions-heading{font-size:18px;font-weight:400;text-transform:uppercase;letter-spacing:-.3px;margin-bottom:6px;white-space:nowrap}
  .positions-heading strong{font-weight:700;color:var(--green-dark)}
  .position-list{list-style:none}
  .position-list li{display:flex;align-items:center;gap:9px;font-size:11.2px;font-weight:700;letter-spacing:-.1px;padding:7px 0;border-bottom:1px solid var(--rule);white-space:nowrap}
  .position-list li:last-child{border-bottom:none}
  .role-icon{flex:none;width:21px;height:21px;border-radius:50%;background:var(--charcoal);border:2px solid #bbb}
  .photo-worker{left:515px;top:950px;width:121px;height:160px;background:linear-gradient(180deg,#b7c8cf 0%,#d7e65a 50%,#2f3c2a 100%)}

  /* footer */
  .cta{position:absolute;left:44px;top:1130px;width:592px;height:40px;display:flex}
  .cta-join{width:196px;background:var(--green-dark);color:var(--paper);font-weight:700;font-size:21px;display:flex;align-items:center;justify-content:center;text-transform:uppercase;letter-spacing:-.3px;white-space:nowrap}
  .cta-contact{flex:1;background:var(--green-lime);display:flex;align-items:center;gap:5px;padding-left:8px;font-weight:700;font-size:15px;letter-spacing:-.2px;color:var(--green-dark);white-space:nowrap}
  .cta-contact svg{flex:none}
  .cta-web{margin-left:4px}
</style>
</head>
<body>
<main class="flyer">

  <div class="brand">
    <span class="brand-ring"></span>
    <span class="brand-name">Ridgeline<br>Contracting<br>Group</span>
  </div>

  <div class="hero-band"></div>
  <h1 class="hero-title">We Are<br>Hiring!</h1>
  <div class="photo photo-crew" role="img" aria-label="Three crew members in high-visibility vests standing on a front lawn"></div>
  <div class="hero-strip"></div>

  <h2 class="adv-heading">Advantages of <strong>Working With Us</strong></h2>
  <ul class="adv-list col-one">
    <li class="tick">Industry Leading Compensation</li>
    <li class="tick">Structured Career Advancement</li>
    <li class="tick">Safe Work Environment</li>
    <li class="tick">Work Promise Policy (Full Time Staff)</li>
    <li class="tick">Health &amp; Dental Benefits</li>
    <li class="tick">Paid Training Programs</li>
    <li class="tick">Paid Clothing Allowance</li>
    <li class="tick">Paid Boot Allowance</li>
    <li class="tick">Positive Culture</li>
    <li class="tick">Progressive Culture</li>
  </ul>
  <span class="col-rule rule-a"></span>
  <ul class="adv-list col-two">
    <li class="tick">Equal Opportunity Employer</li>
    <li class="tick">Veteran Friendly Employer</li>
    <li class="tick">New Equipment</li>
    <li class="tick">Paid Leadership Training</li>
    <li class="tick">Transparent Communication</li>
    <li class="tick">Community Focused</li>
    <li class="tick">Prestigious Clientele</li>
    <li class="tick">Local Work</li>
    <li class="tick">Focused on using industry leading tech</li>
  </ul>
  <span class="col-rule rule-b"></span>
  <ul class="adv-list col-three">
    <li class="tick">Tool Purchase Program</li>
    <li class="tick">Family Atmosphere</li>
    <li class="tick">Team Events (Sports games, Lunches, Get togethers, Etc)</li>
    <li class="tick">Work Life balance</li>
    <li class="tick">Daily On Call Snow Pay</li>
    <li class="dot">Sick Pay</li>
    <li class="plain">Positive reputation</li>
  </ul>

  <div class="side-block side-left"></div>
  <div class="photo photo-paving" role="img" aria-label="Smiling worker holding a power drill beside a paving job"></div>
  <div class="photo photo-yard" role="img" aria-label="Two crew members in safety vests in a backyard with a wheelbarrow"></div>
  <div class="photo photo-van" role="img" aria-label="White company work van with green lettering"></div>
  <div class="side-block side-right"></div>

  <section class="bonus">
    <h3 class="bonus-title">Bonus's Available:</h3>
    <ul class="bonus-list">
      <li>Winter Shift Premium</li>
      <li>Referral Bonus</li>
      <li>Project Incentives</li>
    </ul>
  </section>

  <section class="positions">
    <h3 class="positions-heading">Current <strong>Positions Open:</strong></h3>
    <ul class="position-list">
      <li><span class="role-icon"></span>Winter Crew Members</li>
      <li><span class="role-icon"></span>Salt Truck Driver/Operator (AZ/DZ/AR)</li>
      <li><span class="role-icon"></span>Winter Equipment Operators</li>
      <li><span class="role-icon"></span>Construction Foreperson</li>
    </ul>
  </section>
  <div class="photo photo-worker" role="img" aria-label="Crew member in a safety vest holding a bonus cheque"></div>

  <footer class="cta">
    <div class="cta-join">Join Us Today</div>
    <div class="cta-contact">
      <svg width="14" height="14" viewBox="0 0 24 24" aria-hidden="true"><path d="M6.6 10.8a15.1 15.1 0 0 0 6.6 6.6l2.2-2.2a1 1 0 0 1 1-.25 11.4 11.4 0 0 0 3.6.57 1 1 0 0 1 1 1V20a1 1 0 0 1-1 1A17 17 0 0 1 3 4a1 1 0 0 1 1-1h3.5a1 1 0 0 1 1 1c0 1.250.2 2.45.57 3.57a1 1 0 0 1-.25 1z" fill="none" stroke="#1f6a2f" stroke-width="2"/></svg>
      <span>555-014-7730</span>
      <svg class="cta-web" width="14" height="14" viewBox="0 0 24 24" aria-hidden="true"><g fill="none" stroke="#1f6a2f" stroke-width="2"><circle cx="12" cy="12" r="10"/><path d="M2 12h20M12 2c3 3 3 17 0 20M12 2c-3 3-3 17 0 20"/></g></svg>
      <span>ridgelinecontracting.com</span>
    </div>
  </footer>

</main>
</body>
</html>
```